One Page Sales Flyer for Wireless Survey- Computer Hardware

I want a designer to create a one page 4 color sales slick to be given to our sales team to sell to the end customers. I would like a visual picture of a heat map so zavvix "heat map wireless" to get an idea of how that image should look.

```html
<!DOCTYPE html>
<html lang="en">
<head>
<meta charset="utf-8">
<title>Trestle – Wireless Site Survey Flyer</title>
<link href="https://fonts.googleapis.com/css2?family=Roboto+Condensed:wght@400;700&family=Open+Sans:wght@400;600;700&display=swap" rel="stylesheet">
<style>
:root{
  --page-bg:#c9c9c9;
  --panel-dark:#2b2b2d;
  --panel-dark-2:#3a3b3e;
  --brand-blue:#3a9ddc;
  --paper:#ffffff;
  --ink:#2d2d2d;
  --ink-soft:#4a4a4a;
  --number-blue:#1f5f99;
}
*{margin:0;padding:0;box-sizing:border-box}
html,body{width:800px;height:1200px;overflow:hidden;background:var(--page-bg)}
.flyer{position:absolute;left:20px;top:62px;width:760px;height:1075px;background:var(--paper);box-shadow:0 6px 18px rgba(0,0,0,.35);overflow:hidden}
.sidebar{position:absolute;left:0;top:0;width:376px;height:100%;background:linear-gradient(180deg,var(--panel-dark) 0%,var(--panel-dark-2) 45%,var(--panel-dark) 100%);color:#fff;font-family:"Roboto Condensed",sans-serif}
.globe-backdrop{position:absolute;left:-40px;top:380px;width:440px;height:480px;border-radius:50%;background:radial-gradient(circle at 45% 45%,rgba(255,255,255,.12),rgba(255,255,255,.03) 60%,transparent 72%)}
.brand{position:absolute;left:0;top:70px;width:100%;text-align:center}
.brand-square{display:block;width:100px;height:100px;margin:0 auto;border-radius:12px;background:var(--brand-blue)}
.brand-name{display:block;margin-top:36px;font-weight:400;font-size:52px;letter-spacing:1px;line-height:1}
.headline{position:absolute;left:0;top:330px;width:100%;text-align:center;font-weight:700;line-height:.95}
.headline .line-blue{display:block;color:var(--brand-blue);font-size:92px}
.headline .line-white{display:block;color:#fff;font-size:62px;margin-top:6px}
.tagline{position:absolute;left:26px;top:514px;width:324px;height:30px;background:var(--brand-blue);text-align:center;font-size:21px;line-height:30px;letter-spacing:.5px;font-weight:400}
.customers{position:absolute;left:42px;top:630px}
.customers h2{font-size:30px;font-weight:700;letter-spacing:.5px;margin-bottom:22px}
.customers ul{list-style:none}
.customers li{display:flex;align-items:center;height:35px;font-size:21px;font-family:"Open Sans",sans-serif}
.customers svg{width:17px;height:17px;margin-right:22px;flex:none}
.content{position:absolute;left:376px;top:0;width:384px;height:100%;font-family:"Open Sans",sans-serif;color:var(--ink)}
.section-title{position:absolute;left:40px;width:300px;background:var(--brand-blue);color:#fff;font-weight:700;font-size:15px;line-height:20px;text-align:center;padding:4px 10px}
.section-body{position:absolute;left:40px;width:305px;font-size:13.2px;line-height:19px;text-align:justify;color:var(--ink-soft)}
.points{list-style:none}
.points li{margin-bottom:22px}
.points .num{font-family:"Roboto Condensed",sans-serif;font-weight:700;color:var(--number-blue);font-size:19px;margin-right:4px}
.contact{position:absolute;left:32px;top:852px;width:352px;height:223px;background:var(--brand-blue);padding:30px 0 0 34px}
.contact h2{font-family:"Roboto Condensed",sans-serif;font-weight:700;font-size:40px;color:#1e2024;line-height:1;margin-bottom:26px}
.contact p{display:flex;align-items:center;color:#fff;font-size:14px;height:30px}
.contact svg{width:14px;height:14px;margin-right:14px;flex:none}
</style>
</head>
<body>
<main class="flyer">
  <aside class="sidebar">
    <div class="globe-backdrop" role="img" aria-label="Faint globe and network illustration behind the sidebar"></div>
    <div class="brand">
      <span class="brand-square"></span>
      <span class="brand-name">TRESTLE</span>
    </div>
    <h1 class="headline">
      <span class="line-blue">YOUR</span>
      <span class="line-white">TRESTLE OF</span>
    </h1>
    <div class="tagline">TECHNOLOGY THERAPISTS</div>
    <section class="customers">
      <h2>TARGET CUSTOMERS</h2>
      <ul>
        <li><svg viewBox="0 0 20 20"><circle cx="10" cy="10" r="8.5" fill="none" stroke="#3a9ddc" stroke-width="2"/><path d="M6 10.5l3 3 5-6" fill="none" stroke="#3a9ddc" stroke-width="2"/></svg>Distributors</li>
        <li><svg viewBox="0 0 20 20"><circle cx="10" cy="10" r="8.5" fill="none" stroke="#3a9ddc" stroke-width="2"/><path d="M6 10.5l3 3 5-6" fill="none" stroke="#3a9ddc" stroke-width="2"/></svg>Warehouses</li>
        <li><svg viewBox="0 0 20 20"><circle cx="10" cy="10" r="8.5" fill="none" stroke="#3a9ddc" stroke-width="2"/><path d="M6 10.5l3 3 5-6" fill="none" stroke="#3a9ddc" stroke-width="2"/></svg>SLED</li>
        <li><svg viewBox="0 0 20 20"><circle cx="10" cy="10" r="8.5" fill="none" stroke="#3a9ddc" stroke-width="2"/><path d="M6 10.5l3 3 5-6" fill="none" stroke="#3a9ddc" stroke-width="2"/></svg>K-12</li>
        <li><svg viewBox="0 0 20 20"><circle cx="10" cy="10" r="8.5" fill="none" stroke="#3a9ddc" stroke-width="2"/><path d="M6 10.5l3 3 5-6" fill="none" stroke="#3a9ddc" stroke-width="2"/></svg>Medical / Hospitals</li>
        <li><svg viewBox="0 0 20 20"><circle cx="10" cy="10" r="8.5" fill="none" stroke="#3a9ddc" stroke-width="2"/><path d="M6 10.5l3 3 5-6" fill="none" stroke="#3a9ddc" stroke-width="2"/></svg>Enterprise F1000</li>
        <li><svg viewBox="0 0 20 20"><circle cx="10" cy="10" r="8.5" fill="none" stroke="#3a9ddc" stroke-width="2"/><path d="M6 10.5l3 3 5-6" fill="none" stroke="#3a9ddc" stroke-width="2"/></svg>Sports Venues</li>
        <li><svg viewBox="0 0 20 20"><circle cx="10" cy="10" r="8.5" fill="none" stroke="#3a9ddc" stroke-width="2"/><path d="M6 10.5l3 3 5-6" fill="none" stroke="#3a9ddc" stroke-width="2"/></svg>Stadiums</li>
        <li><svg viewBox="0 0 20 20"><circle cx="10" cy="10" r="8.5" fill="none" stroke="#3a9ddc" stroke-width="2"/><path d="M6 10.5l3 3 5-6" fill="none" stroke="#3a9ddc" stroke-width="2"/></svg>Hotels</li>
        <li><svg viewBox="0 0 20 20"><circle cx="10" cy="10" r="8.5" fill="none" stroke="#3a9ddc" stroke-width="2"/><path d="M6 10.5l3 3 5-6" fill="none" stroke="#3a9ddc" stroke-width="2"/></svg>Retail stores</li>
      </ul>
    </section>
  </aside>

  <section class="content">
    <h3 class="section-title" style="top:46px">WHAT IS A WIRELESS SITE<br>SURVEY OR HEAT MAP?</h3>
    <p class="section-body" style="top:122px">A wireless site survey is a compilation of reports showing a visual representation of health of your wireless network. This does not only show how strong or weak a wireless signal is in any location it also helps aid in channel and placement to ensure maximum stable data rates are archived even where the single appears strong</p>

    <h3 class="section-title" style="top:262px">WHY DO CUSTOMERS NEED A<br>SITE SURVEY?</h3>
    <p class="section-body" style="top:334px">Any variety of factors can contribute to an unhealthy wireless network (electrical, motors, materials used in construction, distance, neighboring wireless networks, etc.) and traditional methods that use only blueprints and a computer program to show signal strength have shown to be ineffective.</p>

    <h3 class="section-title" style="top:464px">WHY SHOULD THEY USE YOU?</h3>
    <ol class="section-body points" style="top:518px">
      <li><span class="num">1.</span>42% of businesses report some issues with wireless connectivity and acknowledge its effect on the bottom line*</li>
      <li><span class="num">2.</span>Most of these problems are solved through either fine tuning the current equipment (managed services) or purchasing new equipment (incremental sales) of which you can provide both</li>
      <li><span class="num">3.</span>Being a one-stop shop for all your customer's IT needs prevents them from needing additional vendors</li>
      <li><span class="num">4.</span>The increase of IoT (Internet of things) and BYOD (Bring Your Own Device)</li>
    </ol>

    <div class="contact">
      <h2>Contact us</h2>
      <p><svg viewBox="0 0 16 16"><circle cx="8" cy="8" r="6.5" fill="none" stroke="#fff" stroke-width="1.5"/><path d="M1.5 8h13M8 1.5c-3 3.5-3 9.5 0 13M8 1.5c3 3.5 3 9.5 0 13" fill="none" stroke="#fff" stroke-width="1.2"/></svg>www.yourtrestle.com</p>
      <p><svg viewBox="0 0 16 16"><rect x="1.5" y="3.5" width="13" height="9" fill="none" stroke="#fff" stroke-width="1.5"/><path d="M1.5 3.5l6.5 5 6.5-5" fill="none" stroke="#fff" stroke-width="1.5"/></svg>info@yourtrestle.com</p>
      <p><svg viewBox="0 0 16 16"><path d="M3 1.5l3 .5 1 3.5-2 1.2c.8 1.8 2 3 3.8 3.8l1.2-2 3.5 1 .5 3c-.5 1-1.5 1.5-2.5 1.5C6 14 2 10 2 4c0-1 .5-2 1-2.5z" fill="#fff"/></svg>555-014-2286</p>
    </div>
  </section>
</main>
</body>
</html>
```